Tick Tock Green Frog

I'm looking for one generic business card that be used for four people or would it be easier to get four different design of cards.

I have attached the logo, of the cow. I would also like to use one colour of the cow's legs in the background.

Info for card:
Dana Holcroft
Wrangler of Opportunities
Phone: 044 718 2094
email: dana.holcroft@ticktockgreenfrogs.com.au
Web: www.ticktockgreenfrogs.com.au

Here is some tag lines that could also be used:

"Hop-ping you in the right direction"

"Putting the Tick Tock back into early childhood"
"Where there is NO croak"

Industry/Entity Type

Business

```html
<!DOCTYPE html>
<html lang="en">
<head>
<meta charset="utf-8">
<title>Tick Tock Green Frog – Business Card</title>
<link rel="stylesheet" href="https://fonts.googleapis.com/css2?family=Lato:wght@400;700;900&display=swap">
<style>
  :root {
    --stage: #1e1e1e;
    --card-white: #ffffff;
    --brand-purple: #3a2067;
    --brand-brown: #4a2a14;
    --leg-green: #6b9a3a;
    --text-light: #ffffff;
  }
  * { box-sizing: border-box; margin: 0; padding: 0; }
  html, body {
    width: 1200px;
    height: 926px;
    overflow: hidden;
    background: var(--stage);
    font-family: "Lato", sans-serif;
  }
  .stage {
    width: 1200px;
    height: 926px;
    display: flex;
    flex-direction: column;
    align-items: center;
    justify-content: center;
    gap: 56px;
  }
  .card {
    width: 700px;
    height: 400px;
    position: relative;
    overflow: hidden;
    box-shadow: 0 10px 30px rgba(0,0,0,0.45);
  }

  /* Front */
  .card-front { background: var(--card-white); }
  .brand-area {
    height: 56%;
    display: flex;
    align-items: center;
    justify-content: center;
    gap: 16px;
  }
  .brand-mark {
    width: 26px;
    height: 26px;
    background: var(--leg-green);
  }
  .brand-name {
    font-weight: 900;
    font-size: 40px;
    color: var(--brand-brown);
    letter-spacing: 0.5px;
  }
  .contact-band {
    position: absolute;
    left: 0; right: 0; bottom: 0;
    height: 44%;
    background: var(--brand-purple);
    color: var(--text-light);
    padding: 22px 0 0 150px;
  }
  .person {
    display: flex;
    align-items: baseline;
    gap: 10px;
    margin-bottom: 16px;
  }
  .person-name {
    font-weight: 900;
    font-size: 27px;
    text-transform: uppercase;
    letter-spacing: 0.5px;
  }
  .person-role {
    font-weight: 700;
    font-size: 17px;
  }
  .contact-list {
    list-style: none;
    font-size: 17px;
    line-height: 1.45;
  }
  .contact-list .label { font-weight: 700; }

  /* Back */
  .card-back {
    background: var(--brand-purple);
    color: var(--text-light);
    display: flex;
    flex-direction: column;
    align-items: center;
    justify-content: center;
    text-align: center;
  }
  .taglines {
    list-style: none;
    font-size: 25px;
    line-height: 1.4;
  }
</style>
</head>
<body>
<main class="stage">
  <section class="card card-front" aria-label="Business card front">
    <div class="brand-area">
      <span class="brand-mark" aria-hidden="true"></span>
      <span class="brand-name">Tick Tock Green Frog</span>
    </div>
    <div class="contact-band">
      <div class="person">
        <span class="person-name">Dana Holcroft</span>
        <span class="person-role">wrangler of opportunities</span>
      </div>
      <ul class="contact-list">
        <li><span class="label">phone</span>: 044 718 2094</li>
        <li><span class="label">web</span>: www.ticktockgreenfrogs.com.au</li>
        <li><span class="label">email</span>: dana.holcroft@ticktockgreenfrogs.com.au</li>
      </ul>
    </div>
  </section>

  <section class="card card-back" aria-label="Business card back">
    <ul class="taglines">
      <li>Hop-ping you in the right direction</li>
      <li>Putting the Tick Tock back into early childhood</li>
      <li>Where there is NO croak</li>
    </ul>
  </section>
</main>
</body>
</html>
```